Responsive web design for leading product search engine

Trovanix is the leading product search engine in Australia and is soon to expand into Asia. We need a lightweight responsive homepage designed for our 3 regional domains. Our domains are Trovanix.com, Trovanix.com.au and Trovanix.asia. We need 3 versions of the same page to appeal to each region. The page and images used need to use a responsive html 5 based web page. The images used in the design need to be responsive and include CSS3 style elements.

For inspiration I would divert you to www.bramvelt.com and www.pinhardo.com.au and I have attached a mockup of what I think it could look like.
Updates

Target Market(s)

Target market is female shoppers 16-40 years old

Industry/Entity Type

Retail

Coding

Coded - Design and coding required

Number of Pages Required

3 page

Colors
33b8a4

Requirements
Must have
• Different image for each of the 3 duplicate pages. 1 for each region Australia (.com.au) Asia (.asia) US (.com). These images must be licensed for public use.

```html
<!DOCTYPE html>
<html lang="en">
<head>
<meta charset="utf-8">
<title>Trovanix – Product Search</title>
<link href="https://fonts.googleapis.com/css2?family=Open+Sans:wght@400;600;700&display=swap" rel="stylesheet">
<style>
:root{
  --teal:#33b8a4;
  --teal-dark:#1f7f71;
  --ink:#3a3a3a;
  --muted:#8a8a8a;
  --light:#eef2f2;
  --footer:#2b2b2b;
  --white:#ffffff;
}
*{box-sizing:border-box;margin:0;padding:0}
html,body{width:1200px;height:2420px;overflow:hidden}
body{font-family:"Open Sans",Arial,sans-serif;color:var(--ink);background:var(--white);position:relative}

.header{height:130px;display:flex;align-items:center;padding:0 100px;justify-content:space-between}
.brand{display:flex;align-items:center;gap:12px;font-size:46px;font-weight:600;color:var(--teal)}
.brand-mark{width:34px;height:34px;border-radius:50%;border:4px solid var(--teal)}
.search{display:flex;height:50px}
.search span{border:1px solid #d6dcdc;font-size:13px;color:#aaa;display:flex;align-items:center;padding:0 14px}
.search .q{width:300px}.search .loc{width:180px;border-left:none}
.search .go{width:56px;background:var(--teal);display:flex;align-items:center;justify-content:center;border:none}

.nav{height:46px;background:var(--teal);display:flex;align-items:center;padding:0 100px;gap:58px;font-size:13px;font-weight:600;color:var(--white)}
.nav .active{border-bottom:2px solid var(--white);padding-bottom:3px}
.nav svg{margin-left:auto}

.hero{position:relative;height:744px;overflow:hidden;
  background:
    radial-gradient(ellipse 320px 380px at 300px 300px,rgba(235,232,226,.55),transparent 70%),
    radial-gradient(ellipse 500px 300px at 900px 120px,rgba(190,200,200,.35),transparent 70%),
    linear-gradient(180deg,#5d6869 0%,#434f51 45%,#2b4744 70%,#1c6a5f 88%,#23907f 100%)}
.hero-text{position:absolute;right:100px;top:168px;text-align:right;color:var(--white)}
.hero-text h1{font-size:46px;font-weight:600;line-height:1.3}
.hero-text .app{position:absolute;left:120px;top:150px;white-space:nowrap;color:var(--teal);font-size:17px;border-bottom:2px solid var(--teal);padding-bottom:4px}
.partners{position:absolute;bottom:48px;left:0;width:100%;display:flex;justify-content:center;gap:150px}
.partner{display:flex;flex-direction:column;align-items:center;gap:12px}
.partner .badge{width:54px;height:54px;border-radius:50%;background:var(--white)}
.partner:nth-child(even) .badge{border-radius:6px;width:50px;height:44px}
.partner .bar{width:60px;height:6px;background:rgba(255,255,255,.85);border-radius:2px}

.discover{position:relative;height:420px}
.phone{position:absolute;left:110px;top:30px;width:190px;height:340px;border-radius:28px;
  background:linear-gradient(165deg,#f4f6f6 0%,#d7dede 8%,#8fb9c9 14%,#6aa7c4 45%,#7c6fbf 70%,#d9e0e0 92%,#c4cccc 100%);
  transform:rotate(-22deg);box-shadow:0 18px 30px rgba(0,0,0,.15)}
.discover-copy{position:absolute;left:520px;top:44px;width:580px}
h2{color:var(--teal);font-size:34px;font-weight:600;line-height:1.2}
.lead{margin-top:18px;font-size:16px;line-height:1.5}
.body{margin-top:16px;font-size:11px;line-height:1.65;color:var(--muted)}
.btn{display:inline-block;margin-top:24px;background:var(--teal);color:var(--white);font-size:11px;font-weight:700;padding:11px 22px}

.variations{position:relative;height:450px}
.variations-copy{position:absolute;left:100px;top:60px;width:400px}
.music-photo{position:absolute;left:560px;top:60px;width:540px;height:320px;
  background:
    radial-gradient(ellipse 140px 160px at 310px 130px,rgba(240,210,190,.9),transparent 70%),
    radial-gradient(ellipse 180px 90px at 330px 290px,rgba(200,50,70,.75),transparent 70%),
    linear-gradient(110deg,#5a2a22 0%,#9a5a44 40%,#d8a890 70%,#efe4dc 100%)}
.play{position:absolute;left:248px;top:138px}

.features{height:380px;background:var(--light);display:flex;justify-content:center;gap:90px;padding-top:60px}
.feature{width:190px;text-align:center}
.ring{width:112px;height:112px;margin:0 auto;border:3px solid var(--teal);border-radius:50%;display:flex;align-items:center;justify-content:center}
.feature h3{margin-top:26px;font-size:13px;font-weight:600;line-height:1.4}
.feature p{margin-top:10px;font-size:10px;line-height:1.6;color:var(--muted)}

.footer{position:absolute;left:0;top:2170px;width:100%;height:250px;background:var(--footer);color:var(--white);padding:40px 100px}
.stores{display:flex;gap:12px}
.stores span{width:120px;height:36px;border-radius:6px;background:#111;border:1px solid #666}
.links{margin-top:20px;font-size:11px;line-height:2;display:grid;grid-template-columns:110px 120px}
.newsletter{position:absolute;left:440px;top:40px}
.newsletter h4{font-size:14px;font-weight:600}
.newsletter p{font-size:10px;color:#aaa;margin-top:4px}
.sub{display:flex;margin-top:16px}
.sub span:first-child{width:230px;height:30px;background:var(--white);font-size:10px;color:#aaa;padding:8px 10px}
.sub span:last-child{background:var(--teal);font-size:10px;font-weight:700;padding:9px 16px}
.social{position:absolute;right:100px;top:76px;display:flex;gap:8px}
.social span{width:44px;height:44px;border-radius:3px}
.copy{position:absolute;left:0;bottom:18px;width:100%;text-align:center;font-size:9px;color:#888}
</style>
</head>
<body>
<header class="header">
  <div class="brand"><span class="brand-mark"></span>Trovanix</div>
  <div class="search">
    <span class="q">Search for products</span>
    <span class="loc">Enter location</span>
    <span class="go"><svg width="16" height="16" viewBox="0 0 16 16"><circle cx="7" cy="7" r="5" fill="none" stroke="#fff" stroke-width="2"/><path d="M11 11l4 4" stroke="#fff" stroke-width="2"/></svg></span>
  </div>
</header>
<nav class="nav">
  <span class="active">HOME</span><span>ABOUT</span><span>PRICE</span><span>PARTNERS</span><span>PLATFORMS</span><span>JOIN US</span><span>HELP</span><span>CONTACT</span>
  <svg width="20" height="18" viewBox="0 0 20 18"><path d="M1 2h3l2 10h11l2-7H6" fill="none" stroke="#fff" stroke-width="2"/><circle cx="8" cy="16" r="1.5" fill="#fff"/><circle cx="16" cy="16" r="1.5" fill="#fff"/></svg>
</nav>
<section class="hero" role="img" aria-label="Woman browsing on a tablet in a busy shopping centre, fading to teal">
  <div class="hero-text">
    <h1>Search millions of products<br>on sale at nearby stores</h1>
    <span class="app">Download The App</span>
  </div>
  <div class="partners">
    <div class="partner"><span class="badge"></span><span class="bar"></span></div>
    <div class="partner"><span class="badge"></span><span class="bar"></span></div>
    <div class="partner"><span class="badge"></span><span class="bar"></span></div>
    <div class="partner"><span class="badge"></span><span class="bar"></span></div>
    <div class="partner"><span class="badge"></span><span class="bar"></span></div>
  </div>
</section>
<section class="discover">
  <div class="phone" role="img" aria-label="Smartphone showing colourful app icons"></div>
  <div class="discover-copy">
    <h2>Discover the best products<br>while you shop</h2>
    <p class="lead">Search every product in every store and you'll never miss out on the latest trends on sale in your area</p>
    <p class="body">Lorem Ipsum is simply dummy text of the printing and typesetting industry. It has been the standard filler text since the early days, used to show how a layout reads before the final copy is ready, and it has survived many changes in print and digital publishing.</p>
    <span class="btn">READ MORE</span>
  </div>
</section>
<section class="variations">
  <div class="variations-copy">
    <h2>There are many variations passages of Lorem.</h2>
    <p class="body">Many shoppers compare prices before they buy. Our search brings together stock from thousands of local stores so you can find the item you want, check the price and pick it up nearby the same day without waiting for delivery.</p>
    <span class="btn">READ MORE</span>
  </div>
  <div class="music-photo" role="img" aria-label="Smiling young woman listening to music on headphones">
    <svg class="play" width="44" height="44" viewBox="0 0 44 44"><circle cx="22" cy="22" r="20" fill="none" stroke="#fff" stroke-width="2"/><path d="M18 14l12 8-12 8z" fill="#fff"/></svg>
  </div>
</section>
<section class="features">
  <div class="feature">
    <div class="ring"><svg width="50" height="50" viewBox="0 0 50 50" fill="none" stroke="#33b8a4" stroke-width="3"><circle cx="25" cy="25" r="18"/><path d="M25 7v36M7 25h36"/></svg></div>
    <h3>NEMO ENIM IPSAM VOLUPTATEM</h3>
    <p>Find stores near you and compare prices in one simple place.</p>
  </div>
  <div class="feature">
    <div class="ring"><svg width="50" height="50" viewBox="0 0 50 50" fill="none" stroke="#33b8a4" stroke-width="3"><path d="M10 40l30-30M10 10l30 30"/></svg></div>
    <h3>ELECTRONIC TYPE-SETTING</h3>
    <p>Browse the latest deals from shops across your city every day.</p>
  </div>
  <div class="feature">
    <div class="ring"><svg width="50" height="50" viewBox="0 0 50 50" fill="none" stroke="#33b8a4" stroke-width="3"><path d="M8 36V20h34v16M8 28h34M14 20v-6h22v6"/></svg></div>
    <h3>MORE OBSCURE LATIN WORDS</h3>
    <p>Save your favourite items and get alerts when prices drop fast.</p>
  </div>
  <div class="feature">
    <div class="ring"><svg width="50" height="50" viewBox="0 0 50 50" fill="none" stroke="#33b8a4" stroke-width="3"><circle cx="25" cy="19" r="8"/><path d="M11 42c2-9 8-13 14-13s12 4 14 13"/></svg></div>
    <h3>LOREM IPSUM, "LOREM</h3>
    <p>Join thousands of shoppers who already find better deals nearby.</p>
  </div>
</section>
<footer class="footer">
  <div class="stores"><span></span><span></span></div>
  <div class="links"><span>About</span><span>Privacy Policy</span><span>Terms of Service</span><span>Contact Us</span></div>
  <div class="newsletter">
    <h4>SIGN TO NEWSLETTER</h4>
    <p>Get our best deals in your inbox</p>
    <div class="sub"><span>Email address</span><span>SUBSCRIBE</span></div>
  </div>
  <div class="social"><span style="background:#3b5998"></span><span style="background:#29a9e1"></span><span style="background:#d34836"></span><span style="background:#1f7bc1"></span></div>
  <p class="copy">Copyright © 2015 Trovanix.com. All rights reserved.</p>
</footer>
</body>
</html>
```